Business Card Design - Carrington Hill Lodge

We are looking at a new design for our business cards that has a modern and professional look. We run a residential aged care facility focussing on the care of residents. The cards will be used for potential clients, consultants and business opportunities in this sector. Blue and white is our main colours and would to see these colours incorporated in the design.
Industry/Entity Type
Business
Contact Information for Business Card
Carrington Hill Lodge, Darren Pelham, dpelham@carringtonhilllodge.com.au, Finance Manager, 0491 736 208, BCom, 48 Yarrabee Way, Kelvin Ridge, Qld 4215.

```html
<!DOCTYPE html>
<html lang="en">
<head>
<meta charset="utf-8">
<title>Carrington Hill Lodge – Business Card</title>
<link rel="stylesheet" href="https://fonts.googleapis.com/css2?family=Cinzel:wght@500&family=Open+Sans:wght@400;600&display=swap">
<style>
  :root {
    --backdrop: #2c2e33;
    --card: #dfe7ea;
    --brand-blue: #4b7892;
    --tan: #a89a90;
    --ink: #1f2326;
    --card-w: 560px;
    --card-h: 342px;
  }
  * { box-sizing: border-box; margin: 0; padding: 0; }
  html, body {
    width: 1200px;
    height: 864px;
    overflow: hidden;
    background: var(--backdrop);
  }
  .canvas {
    width: 1200px;
    height: 864px;
    display: flex;
    flex-direction: column;
    align-items: center;
    justify-content: center;
    gap: 44px;
  }
  .card {
    width: var(--card-w);
    height: var(--card-h);
    background: var(--card);
    position: relative;
    overflow: hidden;
  }

  /* Front */
  .card--front {
    display: flex;
    flex-direction: column;
    align-items: center;
    justify-content: center;
    gap: 14px;
  }
  .brand {
    display: flex;
    align-items: center;
    gap: 14px;
  }
  .brand__square {
    width: 22px;
    height: 22px;
    background: var(--brand-blue);
  }
  .brand__name {
    font-family: "Open Sans", sans-serif;
    font-weight: 400;
    font-size: 30px;
    letter-spacing: 3px;
    text-transform: uppercase;
    color: var(--brand-blue);
  }
  .tagline {
    font-family: "Open Sans", sans-serif;
    font-size: 15px;
    letter-spacing: 0.5px;
    color: var(--tan);
  }

  /* Back */
  .card--back {
    display: flex;
    flex-direction: column;
    align-items: center;
    padding-top: 36px;
    text-align: center;
  }
  .person__name {
    font-family: "Cinzel", serif;
    font-weight: 500;
    font-size: 29px;
    color: var(--brand-blue);
    letter-spacing: 0.5px;
  }
  .person__role {
    font-family: "Open Sans", sans-serif;
    font-size: 16px;
    color: var(--ink);
    margin-top: 2px;
  }
  .address {
    font-family: "Open Sans", sans-serif;
    font-style: normal;
    font-size: 17px;
    line-height: 1.35;
    color: var(--ink);
    margin-top: 42px;
  }
  .contact {
    list-style: none;
    font-family: "Open Sans", sans-serif;
    font-size: 18px;
    color: var(--ink);
    margin-top: 40px;
    line-height: 1.3;
  }
  .contact__item {
    display: flex;
    align-items: center;
    justify-content: center;
    gap: 6px;
  }
  .contact__icon {
    width: 17px;
    height: 17px;
    fill: var(--brand-blue);
  }
</style>
</head>
<body>
<main class="canvas">
  <section class="card card--front" aria-label="Card front">
    <div class="brand">
      <span class="brand__square"></span>
      <span class="brand__name">Carrington Hill Lodge</span>
    </div>
    <p class="tagline">Comfort, Respect, Belonging</p>
  </section>

  <section class="card card--back" aria-label="Card back">
    <h1 class="person__name">Darren Pelham, BCom</h1>
    <p class="person__role">Finance Manager</p>
    <address class="address">
      48 Yarrabee Way,<br>
      Kelvin Ridge, Qld 4215
    </address>
    <ul class="contact">
      <li class="contact__item">
        <svg class="contact__icon" viewBox="0 0 24 24" aria-hidden="true">
          <path d="M6.6 10.8a15.1 15.1 0 0 0 6.6 6.6l2.2-2.2a1 1 0 0 1 1-.25 11.4 11.4 0 0 0 3.6.57 1 1 0 0 1 1 1V20a1 1 0 0 1-1 1A17 17 0 0 1 3 4a1 1 0 0 1 1-1h3.5a1 1 0 0 1 1 1c0 1.25.2 2.45.57 3.57a1 1 0 0 1-.25 1z"/>
        </svg>
        0491 736 208
      </li>
      <li class="contact__item">
        <svg class="contact__icon" viewBox="0 0 24 24" aria-hidden="true">
          <path d="M2 5h20v14H2z M4 7v.4l8 5.2 8-5.2V7z" fill-rule="evenodd"/>
        </svg>
        dpelham@carringtonhilllodge.com.au
      </li>
    </ul>
  </section>
</main>
</body>
</html>
```